Investment Advisor E-Newsletter Banner Design

I need a banner designed for an email newsletter that will be sent monthly to clients and prospects. We want to see designs that are elegant and use our logo well. The banner should be 922x150px and should go well with the www.bhtlwest.com website. Should include Logo and email and phone number.

Target Market(s)

High net worth investors

Number of Pages Required

1 page

Requirements
Must have
• logo, place for email (info@bhtlwest.com) and phone number (555-219-0387), colors and design that work well with www.bhtlwest.com website

```html
<!DOCTYPE html>
<html lang="en">
<head>
<meta charset="utf-8">
<title>Bluehaven Trust &amp; Ledger — Newsletter Banner</title>
<link rel="stylesheet" href="https://fonts.googleapis.com/css2?family=Crimson+Text:ital,wght@1,400&display=swap">
<style>
  :root {
    --navy-deep: #0a1852;
    --navy-mid: #123590;
    --navy-glow: #1d4cb3;
    --pill-top: #1c2766;
    --pill-bottom: #0b1240;
    --white: #ffffff;
    --photo-light: #c9c7c2;
    --photo-dark: #6e6a66;
    --icon-ink: #141c4e;
  }
  html, body {
    margin: 0;
    padding: 0;
    overflow: hidden;
    background: var(--white);
  }
  .banner {
    position: relative;
    width: 1200px;
    height: 195px;
    overflow: hidden;
    background:
      radial-gradient(ellipse 420px 200px at 560px 90px, var(--navy-glow) 0%, transparent 70%),
      linear-gradient(100deg, var(--navy-mid) 0%, var(--navy-deep) 55%, var(--navy-mid) 80%, var(--navy-deep) 100%);
    font-family: "Crimson Text", "Times New Roman", serif;
    font-style: italic;
    color: var(--white);
  }
  .banner__photo {
    position: absolute;
    left: 0;
    top: 0;
    width: 300px;
    height: 195px;
  }
  .brand {
    position: absolute;
    left: 312px;
    top: 52px;
    display: flex;
    align-items: center;
    gap: 16px;
  }
  .brand__dot {
    width: 44px;
    height: 44px;
    border-radius: 50%;
    background: var(--white);
    flex: none;
  }
  .brand__name {
    margin: 0;
    font-weight: 400;
    line-height: 1;
    color: var(--white);
  }
  .brand__main {
    display: block;
    font-size: 38px;
  }
  .brand__sub {
    display: block;
    font-size: 17px;
    margin-top: 8px;
  }
  .contact {
    position: absolute;
    top: 65px;
    height: 62px;
    box-sizing: border-box;
    border: 2px solid var(--white);
    border-radius: 31px;
    background: linear-gradient(180deg, var(--pill-top), var(--pill-bottom));
    display: flex;
    align-items: center;
    padding-left: 14px;
    gap: 22px;
    font-size: 23px;
    color: var(--white);
    text-decoration: none;
  }
  .contact--email { left: 634px; width: 277px; }
  .contact--phone { left: 924px; width: 247px; }
  .contact__icon {
    width: 36px;
    height: 36px;
    border-radius: 50%;
    background: var(--white);
    display: flex;
    align-items: center;
    justify-content: center;
    flex: none;
  }
</style>
</head>
<body>
  <div class="banner">
    <svg class="banner__photo" viewBox="0 0 300 195" role="img" aria-label="Photo of advisors in a business meeting around a table">
      <defs>
        <linearGradient id="photoTone" x1="0" y1="0" x2="1" y2="1">
          <stop offset="0" stop-color="var(--photo-light)"/>
          <stop offset="1" stop-color="var(--photo-dark)"/>
        </linearGradient>
      </defs>
      <path d="M0,0 H256 Q300,97 236,195 H0 Z" fill="url(#photoTone)"/>
      <path d="M256,0 Q300,97 236,195" fill="none" stroke="var(--white)" stroke-width="7"/>
    </svg>

    <div class="brand">
      <span class="brand__dot"></span>
      <h1 class="brand__name">
        <span class="brand__main">Bluehaven Trust</span>
        <span class="brand__sub">Ledger &amp; Research, Inc.</span>
      </h1>
    </div>

    <a class="contact contact--email" href="mailto:info@bhtlwest.com">
      <span class="contact__icon">
        <svg width="18" height="14" viewBox="0 0 18 14" aria-hidden="true">
          <rect x="0" y="0" width="18" height="14" rx="1.5" fill="var(--icon-ink)"/>
          <path d="M1,1.5 L9,8 L17,1.5" fill="none" stroke="var(--white)" stroke-width="1.4"/>
        </svg>
      </span>
      info@bhtlwest.com
    </a>

    <a class="contact contact--phone" href="tel:5552190387">
      <span class="contact__icon">
        <svg width="18" height="18" viewBox="0 0 24 24" aria-hidden="true">
          <path fill="var(--icon-ink)" d="M6.6 10.8a15.1 15.1 0 0 0 6.6 6.6l2.2-2.2a1 1 0 0 1 1-.25 11.4 11.4 0 0 0 3.6.57 1 1 0 0 1 1 1V20a1 1 0 0 1-1 1A17 17 0 0 1 3 4a1 1 0 0 1 1-1h3.5a1 1 0 0 1 1 1c0 1.25.2 2.45.57 3.57a1 1 0 0 1-.25 1z"/>
        </svg>
      </span>
      555-219-0387
    </a>
  </div>
</body>
</html>
```